Stationery Design Project

We are looking for a full revision of our existing stationary to include within this project:

- Letterhead
- Business card
- Compliment slip

The items should be a reflection of our new website which can be found at http://www.brackenledger.co.uk/

Our logo files are included within the file brief

There are some further projects which we may approach the winning designer for as we need a revision to the front cover of our reports, a new price list and two brochures for specific target markets.

Industry/Entity Type

Business

```html
<!DOCTYPE html>
<html lang="en">
<head>
<meta charset="utf-8">
<title>Bracken Ledger — Business Card</title>
<link href="https://fonts.googleapis.com/css2?family=PT+Sans:ital,wght@0,400;0,700;1,700&display=swap" rel="stylesheet">
<style>
  :root {
    --backdrop: #2e3436;
    --card: #ffffff;
    --navy: #29265f;
    --royal: #1d55a6;
    --ink: #1f1f1f;
    --muted: #3a3a3a;
  }
  * { margin: 0; padding: 0; box-sizing: border-box; }
  html, body {
    width: 971px; height: 1200px; overflow: hidden;
    background: var(--backdrop);
    font-family: "PT Sans", sans-serif;
  }
  .canvas { position: relative; width: 971px; height: 1200px; }
  .card {
    position: absolute; width: 800px; height: 457px;
    background: var(--card); border-radius: 28px; overflow: hidden;
  }
  .card--front { left: 85px; top: 97px; }
  .card--back { left: 81px; top: 642px; }

  .wordmark {
    position: absolute; left: 0; width: 100%;
    display: flex; align-items: center; justify-content: center; gap: 18px;
  }
  .wordmark__name {
    font-weight: 400; font-size: 74px; letter-spacing: 1px;
    color: var(--navy); text-transform: uppercase; line-height: 1;
  }
  .wordmark__dot {
    width: 16px; height: 16px; border-radius: 50%; background: var(--navy);
  }
  .card--front .wordmark { top: 170px; }
  .card--back .wordmark { top: 170px; }

  .contact-band { position: absolute; left: 0; top: 290px; width: 800px; height: 99px; }
  .contact-band svg { position: absolute; inset: 0; }
  .holder {
    position: absolute; left: 64px; top: 24px; color: #fff;
  }
  .holder__name { font-weight: 700; font-size: 24px; line-height: 1.2; }
  .holder__role { font-size: 19px; line-height: 1.3; }
  .links {
    position: absolute; right: 59px; top: 25px; color: #fff;
    font-size: 19px; line-height: 26px; text-align: right;
  }
  .label { font-weight: 700; font-style: italic; }

  .address-line {
    position: absolute; left: 0; width: 100%; top: 408px;
    text-align: center; font-size: 19px; color: var(--ink);
  }
  .address-line .sep { margin: 0 6px; }
  .site {
    position: absolute; left: 0; width: 100%; top: 384px;
    text-align: center; font-size: 19px; color: var(--muted);
  }
</style>
</head>
<body>
<div class="canvas">
  <section class="card card--front">
    <div class="wordmark">
      <span class="wordmark__name">Bracken Ledger</span>
      <span class="wordmark__dot"></span>
    </div>
    <div class="contact-band">
      <svg width="800" height="99" viewBox="0 0 800 99">
        <polygon points="0,0 365,0 275,99 0,99" fill="var(--navy)"/>
        <polygon points="380,0 800,0 800,99 292,99" fill="var(--royal)"/>
      </svg>
      <div class="holder">
        <div class="holder__name">Your Name</div>
        <div class="holder__role">Designation</div>
      </div>
      <div class="links">
        <div><span class="label">e</span> : mail@brackenledger.co.uk</div>
        <div><span class="label">w</span> : www.brackenledger.co.uk</div>
      </div>
    </div>
    <p class="address-line"><span class="label">t</span> : 01632 960 418<span class="sep">|</span>123 Street, Suit #123, Your City, State 1234</p>
  </section>

  <section class="card card--back">
    <div class="wordmark">
      <span class="wordmark__name">Bracken Ledger</span>
      <span class="wordmark__dot"></span>
    </div>
    <p class="site">www.brackenledger.co.uk</p>
  </section>
</div>
</body>
</html>
```